Professional Business Cards

We need a nice looking, profession and modern business card for our new company. Our logo is attatched

Target Market(s)

Young Professionals

Industry/Entity Type

Financial

Contact Information for Business Card

FRONT

Morvane Tally Pty Ltd
Level 22, Halden Court, 48 Wirrapool St
Sydney NSW 2000
ABN : 57 304 918 226

Derek Wallis - Chief Operations Officer
P : 02 7153 2819
M: 0418 395 207
derek@morvanetally,com

BACK

- Cryptocurrency Exchange Services
- Cryptocurrency Mining Operations
- Cryptocurrency Investment Fund Offering

Font styles to use
Sans Serif

Colors
0255a3
9d9d9d

```html
<!DOCTYPE html>
<html lang="en">
<head>
<meta charset="utf-8">
<title>Morvane Tally – Business Cards</title>
<link href="https://fonts.googleapis.com/css2?family=Lato:wght@300;400;700&display=swap" rel="stylesheet">
<style>
  :root {
    --brand-blue: #0255a3;
    --band-blue: #1b74c4;
    --brand-grey: #9d9d9d;
    --text-grey: #6a6a6a;
    --card-white: #ffffff;
    --card-white-shade: #e9eaec;
    --card-dark: #6b6b6b;
    --card-dark-shade: #4e4e4e;
    --backdrop: #d9d6d0;
    --light-text: #e6e6e6;
  }
  * { margin: 0; padding: 0; box-sizing: border-box; }
  html, body { width: 1200px; height: 780px; overflow: hidden; }
  body {
    background: var(--backdrop);
    font-family: "Lato", "Helvetica Neue", Arial, sans-serif;
    position: relative;
  }
  .card {
    position: absolute;
    width: 525px;
    height: 300px;
    border-radius: 3px;
    box-shadow: 0 10px 24px rgba(0,0,0,0.22);
    overflow: hidden;
  }

  /* Front */
  .card-front {
    left: 60px; top: 70px;
    background: linear-gradient(120deg, var(--card-white-shade) 0%, var(--card-white) 45%, var(--card-white) 100%);
  }
  .front-brand {
    position: absolute; left: 34px; top: 0; width: 210px; height: 256px;
    display: flex; align-items: center; gap: 10px;
  }
  .brand-square {
    width: 26px; height: 26px; background: var(--brand-blue); flex: none;
  }
  .brand-name {
    color: var(--brand-blue);
    font-weight: 700; font-size: 24px; letter-spacing: 1px; line-height: 1;
  }
  .front-divider {
    position: absolute; left: 258px; top: 44px; width: 1.5px; height: 150px;
    background: var(--band-blue);
  }
  .contact {
    position: absolute; left: 282px; top: 34px; color: var(--text-grey);
    font-size: 13px; line-height: 1.45;
  }
  .contact-name { color: var(--band-blue); font-size: 19px; font-weight: 400; line-height: 1.1; }
  .contact-title { font-size: 12.5px; font-weight: 300; margin-bottom: 12px; }
  .contact-line { display: flex; align-items: center; gap: 7px; font-weight: 300; }
  .contact-line svg { width: 14px; height: 14px; flex: none; }
  .contact-company { font-size: 14px; font-weight: 300; margin-top: 6px; }
  .contact-abn { color: var(--band-blue); font-size: 12.5px; }
  .address-band {
    position: absolute; left: 0; right: 0; bottom: 0; height: 44px;
    background: var(--band-blue);
    color: #fff; font-size: 13.5px; font-weight: 400;
    display: flex; align-items: center; justify-content: center;
    letter-spacing: 0.2px;
  }

  /* Back */
  .card-back {
    left: 615px; top: 400px;
    background: linear-gradient(135deg, var(--card-dark) 0%, #7a7a7a 45%, var(--card-dark-shade) 100%);
    color: var(--light-text);
  }
  .back-brand {
    position: absolute; left: 0; right: 0; top: 92px;
    display: flex; justify-content: center; align-items: center; gap: 12px;
  }
  .back-brand .brand-square { background: #f2f2f2; width: 30px; height: 30px; }
  .back-brand .brand-name { color: #f2f2f2; font-size: 30px; }
  .services {
    position: absolute; left: 0; right: 0; top: 170px;
    text-align: center; font-size: 13px; font-weight: 300; line-height: 1.6;
    color: var(--light-text);
  }
</style>
</head>
<body>

<section class="card card-front" aria-label="Business card front">
  <div class="front-brand">
    <span class="brand-square"></span>
    <span class="brand-name">MORVANE TALLY</span>
  </div>
  <div class="front-divider"></div>
  <div class="contact">
    <p class="contact-name">Derek Wallis</p>
    <p class="contact-title">Chief Operations Officer</p>
    <p class="contact-line">
      <svg viewBox="0 0 14 14" aria-hidden="true"><circle cx="7" cy="7" r="7" fill="#0255a3"/><path d="M4.6 3.6l1.3 1.5-.7.9c.5 1 1.3 1.8 2.3 2.3l.9-.7 1.5 1.3-.8 1.3C6.6 10 4 7.4 3.8 4.4z" fill="#fff"/></svg>
      02 7153 2819
    </p>
    <p class="contact-line">
      <svg viewBox="0 0 14 14" aria-hidden="true"><circle cx="7" cy="7" r="7" fill="#0255a3"/><rect x="5" y="3.2" width="4" height="7.6" rx="0.8" fill="#fff"/><rect x="5.7" y="4.2" width="2.6" height="4.8" fill="#0255a3"/></svg>
      0418 395 207
    </p>
    <p class="contact-line">
      <svg viewBox="0 0 14 14" aria-hidden="true"><circle cx="7" cy="7" r="7" fill="#0255a3"/><rect x="3.6" y="4.5" width="6.8" height="5" fill="#fff"/><path d="M3.6 4.5L7 7.4l3.4-2.9" stroke="#0255a3" stroke-width="0.8" fill="none"/></svg>
      derek@morvanetally,com
    </p>
    <p class="contact-company">Morvane Tally Pty Ltd</p>
    <p class="contact-abn">ABN : 57 304 918 226</p>
  </div>
  <div class="address-band">Level 22, Halden Court, 48 Wirrapool St, Sydney NSW 2000</div>
</section>

<section class="card card-back" aria-label="Business card back">
  <div class="back-brand">
    <span class="brand-square"></span>
    <span class="brand-name">MORVANE TALLY</span>
  </div>
  <div class="services">
    <p>Cryptocurrency Exchange Services | Cryptocurrency Mining Operations</p>
    <p>Cryptocurrency Investment Fund Offering</p>
  </div>
</section>

</body>
</html>
```